Upgrade 4 Images - Bid 1, then we can discuss the other 3

We have a four graphics that we use in various presentations and business proposals. We want to upgrade them to make them really pop and match the level of service we provide, without going overboard.

We're open to new ideas, but the general form and content should stay the same.

I'd like to have all four designed by the same person, but I'm assuming this bid will be for 1 of the four, and then the other three can be contracted as additions.

```html
<!DOCTYPE html>
<html lang="en">
<head>
<meta charset="utf-8">
<title>Service Maturity Stages</title>
<link href="https://fonts.googleapis.com/css2?family=Archivo:wght@700;800&family=Source+Sans+3:wght@400&display=swap" rel="stylesheet">
<style>
  :root {
    --orange: #ee8333;
    --teal: #033f3f;
    --paper: #ffffff;
    --line: 5px;
  }
  html, body {
    margin: 0;
    padding: 0;
    width: 1200px;
    height: 258px;
    overflow: hidden;
    background: var(--paper);
  }
  .stages {
    display: block;
    width: 1200px;
    height: 258px;
  }
  .stage { filter: drop-shadow(3px 4px 4px rgba(0,0,0,0.18)); }
  .outline { fill: none; stroke-width: var(--line); stroke-linejoin: miter; stroke-linecap: butt; }
  .stage--orange .outline { stroke: var(--orange); }
  .stage--teal .outline { stroke: var(--teal); }
  .stage--orange .accent { fill: var(--orange); }
  .stage--teal .accent { fill: var(--teal); }
  .stage-title {
    font-family: "Archivo", "Arial Black", sans-serif;
    font-weight: 800;
    font-size: 52px;
    letter-spacing: 4px;
    text-anchor: middle;
  }
  .stage-item {
    font-family: "Source Sans 3", "Myriad Pro", sans-serif;
    font-size: 23px;
    fill: var(--paper);
    text-anchor: middle;
  }
</style>
</head>
<body>
<svg class="stages" viewBox="0 0 2560 550" role="img" aria-label="Four stages: Ad Hoc, Specialist, Factory, Enterprise">

  <!-- Stage 1 -->
  <g class="stage stage--orange" transform="translate(470,0)">
    <path class="outline" d="M -140 97 A 225 225 0 1 1 -170 420 L -252 420 L -252 215 L -292 250 L -335 205 L -242 128 L -170 128"/>
    <circle class="accent" cx="-140" cy="97" r="13"/>
    <path class="accent" d="M -183 275 L -15 275 L 0 258 L 15 275 L 180 275 A 181.5 181.5 0 0 1 -183 275 Z"/>
    <text class="stage-title accent" x="0" y="245">AD HOC</text>
    <text class="stage-item" x="0" y="307">Easy to Use</text>
    <text class="stage-item" x="0" y="344">Reduced Errors</text>
    <text class="stage-item" x="0" y="380">Job Queue</text>
    <text class="stage-item" x="0" y="416">24 Hour Window</text>
  </g>

  <!-- Stage 2 -->
  <g class="stage stage--teal" transform="translate(1043,0)">
    <path class="outline" d="M -138 97 A 225 225 0 1 1 -173 412 L -328 412 L -328 360 C -223 270 -198 250 -198 215 C -198 175 -253 175 -285 215 L -331 160 C -303 120 -223 110 -165 128"/>
    <path class="outline" d="M -185 318 L -225 350 L -185 350"/>
    <circle class="accent" cx="-138" cy="97" r="13"/>
    <path class="accent" d="M -183 275 L -15 275 L 0 258 L 15 275 L 180 275 A 181.5 181.5 0 0 1 -183 275 Z"/>
    <text class="stage-title accent" x="0" y="245">SPECIALIST</text>
    <text class="stage-item" x="0" y="306">Workflow</text>
    <text class="stage-item" x="0" y="343">Architecture</text>
    <text class="stage-item" x="0" y="380">Search Strategy</text>
    <text class="stage-item" x="0" y="417">Case Reporting</text>
  </g>

  <!-- Stage 3 -->
  <g class="stage stage--orange" transform="translate(1617,0)">
    <path class="outline" d="M -137 97 A 225 225 0 1 1 -172 410 C -197 415 -267 420 -327 405 L -327 340 C -267 360 -197 360 -197 330 C -197 305 -217 292 -282 295 L -282 240 C -227 245 -197 240 -197 215 C -197 175 -257 180 -292 200 L -327 145 C -307 125 -237 110 -172 122"/>
    <circle class="accent" cx="-137" cy="97" r="13"/>
    <path class="accent" d="M -183 275 L -15 275 L 0 258 L 15 275 L 180 275 A 181.5 181.5 0 0 1 -183 275 Z"/>
    <text class="stage-title accent" x="0" y="245">FACTORY</text>
    <text class="stage-item" x="0" y="303">Case Onboarding</text>
    <text class="stage-item" x="0" y="341">Roles</text>
    <text class="stage-item" x="0" y="380">Data Re-use</text>
    <text class="stage-item" x="0" y="419">Resource Mngmt</text>
  </g>

  <!-- Stage 4 -->
  <g class="stage stage--teal" transform="translate(2205,0)">
    <path class="outline" d="M -137 97 A 222 222 0 1 1 -165 412 L -212 412 L -212 355 L -330 355 L -330 298 L -210 120 L -160 120"/>
    <path class="outline" d="M -212 218 L -262 298 L -212 298 Z"/>
    <circle class="accent" cx="-137" cy="97" r="13"/>
    <path class="accent" d="M -183 275 L -15 275 L 0 258 L 15 275 L 180 275 A 181.5 181.5 0 0 1 -183 275 Z"/>
    <text class="stage-title accent" x="0" y="245">ENTERPRISE</text>
    <text class="stage-item" x="0" y="303">Cross-Case Analytics</text>
    <text class="stage-item" x="0" y="341">Data Lakes</text>
    <text class="stage-item" x="0" y="380">Matrixed Use</text>
    <text class="stage-item" x="0" y="419">Recurring Jobs</text>
  </g>

</svg>
</body>
</html>
```